Business Card Design/Stationary Design

We would like designers to submit cool, hip business card designs (plus stationary designs) for a new, upstart software development company located in Toronto.
If you have any questions, please email us.
For inspiration on designs:
http://cardmuse.example/cool-business-cards/
http://layoutnotes.example/2008/05/36-cool-business-cards-you-should%E2%80%99ve-seen.html
http://gigharbor.example/general/18-smokin-hot-business-card-designs/

Card info:

Selvakumar (Selv) Nadarasan

Founder and CEO

47 Brindle Court, Suite 311

Toronto, ON M4K 2T8

Phone: 647-512-7730

Mobile: 416-273-5094

Fax: 647-512-7731

Email: selvakumar.nadarasan@mailbrook.example

www.quendrix.example
Updates

Hi everyone,

In terms of all the designs I have seen so far, here is what I like:

1.  I really like the "back" part of this design.  The "front" looks pretty decent as well, but for the "front", look at #2 on this list.  I like that.

http://www.pitchboard.example/image.aspx?imageLocation=1000_10001_2000_image.jpg&type=design300px&whiteLabelCustId=9999

2. "Side 1" of this I like, the front needs to be reworked.

http://www.pitchboard.example/image.aspx?imageLocation=1000_10002_2000_image.png&type=design300px&whiteLabelCustId=9999

3. http://www.pitchboard.example/image.aspx?imageLocation=1000_10003_2000_image.jpg&type=design300px&whiteLabelCustId=9999

4. http://www.pitchboard.example/image.aspx?imageLocation=1000_10004_2000_image.jpg&type=design300px&whiteLabelCustId=9999

Target Market(s)

We are focused on enterprise customers right now, so businesses with a long-term goal of also reaching out to the consumer market as well.

Industry/Entity Type

Software

Requirements
Must have
• Must look cool, ultra-modern, clean and eye-catching. Must incorporate our logo and the colors found in the logo.

```html
<!DOCTYPE html>
<html lang="en">
<head>
<meta charset="utf-8">
<title>Quendrix Technologies Inc. — Letterhead</title>
<link rel="stylesheet" href="https://fonts.googleapis.com/css2?family=Arimo:ital,wght@0,400;1,400&family=Montserrat:wght@400&display=swap">
<style>
  :root {
    --header-dark: #221f1e;
    --header-mid: #3a3735;
    --header-light: #4a4745;
    --accent-lime: #c7d31c;
    --band-green: #93b12e;
    --band-green-light: #a9c020;
    --footer-lime: #bccb0c;
    --rule-grey: #9b9b9b;
    --rule-silver: #d4d4d4;
    --text-light: #ffffff;
    --text-dark: #1d1d1b;
    --paper: #ffffff;
    --artwork-tone: #f3f4f5;
  }
  * { margin: 0; padding: 0; box-sizing: border-box; }
  html, body { width: 849px; height: 1200px; overflow: hidden; background: var(--paper); }
  .letterhead {
    position: relative;
    width: 849px;
    height: 1200px;
    background: var(--paper);
    font-family: "Arimo", Arial, sans-serif;
  }
  .masthead {
    position: absolute; left: 0; top: 0;
    width: 849px; height: 135px;
    background: linear-gradient(90deg, var(--header-dark) 0%, var(--header-mid) 45%, var(--header-light) 100%);
  }
  .masthead::before {
    content: ""; position: absolute; left: 0; top: 82px;
    width: 2px; height: 53px; background: var(--band-green);
  }
  .contact-block {
    position: absolute; left: 20px; top: 17px;
    color: var(--text-light); font-size: 14px; line-height: 17px;
  }
  .contact-block p { white-space: nowrap; }
  .contact-block .address { margin-bottom: 15px; }
  .contact-block .phones p { line-height: 20px; }
  .accent { color: var(--accent-lime); }
  .brand {
    position: absolute; right: 38px; top: 30px;
    display: flex; align-items: center; gap: 18px;
  }
  .brand-mark {
    width: 62px; height: 62px; border-radius: 50%;
    background: var(--accent-lime);
  }
  .brand-name {
    font-family: "Montserrat", Arial, sans-serif;
    color: var(--text-light);
    font-size: 40px; line-height: 1; letter-spacing: 1px;
  }
  .brand-tagline {
    font-family: "Montserrat", Arial, sans-serif;
    color: var(--text-light);
    font-size: 11px; letter-spacing: 2.2px; text-align: right;
    margin-top: 6px;
  }
  .header-rule {
    position: absolute; left: 0; top: 135px; width: 849px; height: 4px;
    background: linear-gradient(90deg, var(--rule-grey), var(--rule-silver) 60%, var(--rule-grey));
  }
  .header-band {
    position: absolute; left: 0; top: 139px; width: 849px; height: 16px;
    background: var(--band-green);
  }
  .backdrop-artwork {
    position: absolute; left: 0; top: 720px; width: 710px; height: 445px;
    background: radial-gradient(ellipse at 40% 60%, var(--artwork-tone) 0%, rgba(243,244,245,0.5) 45%, rgba(255,255,255,0) 75%);
  }
  .footer-rule {
    position: absolute; left: 0; top: 1164px; width: 849px; height: 4px;
    background: linear-gradient(90deg, var(--rule-grey), #5e5e5e 40%, var(--rule-silver) 60%, var(--rule-grey));
  }
  .footer-band {
    position: absolute; left: 0; top: 1168px; width: 849px; height: 32px;
    background: linear-gradient(180deg, var(--footer-lime) 0%, var(--band-green-light) 100%);
    display: flex; justify-content: space-between; align-items: center;
    padding: 0 11px 0 17px;
    color: var(--text-dark); font-size: 13.5px;
  }
  .footer-band .website { font-style: italic; }
</style>
</head>
<body>
  <div class="letterhead">
    <header class="masthead">
      <div class="contact-block">
        <div class="address">
          <p><span class="accent">47</span> Brindle Court, Suite 311</p>
          <p>Toronto, ON M4K 2T8</p>
        </div>
        <div class="phones">
          <p>Phone: <span class="accent">647</span>-512-7730</p>
          <p>Mobile: <span class="accent">416</span>-273-5094</p>
          <p>Fax: <span class="accent">647</span>-512-7731</p>
        </div>
      </div>
      <div class="brand">
        <div class="brand-mark"></div>
        <div>
          <div class="brand-name">Quendrix</div>
          <div class="brand-tagline">TECHNOLOGIES INC.</div>
        </div>
      </div>
    </header>
    <div class="header-rule"></div>
    <div class="header-band"></div>

    <div class="backdrop-artwork" role="img" aria-label="Faint grey wireframe illustration of concentric curved segments radiating across the lower page"></div>

    <div class="footer-rule"></div>
    <footer class="footer-band">
      <span class="website">www.quendrix.example</span>
      <span class="email">Email: selvakumar.nadarasan@mailbrook.example</span>
    </footer>
  </div>
</body>
</html>
```